Flyer Design for catering company "Rosemary's Larder"

We need a flyer design for a small catering company based in Melbourne, Australia called Rosemary's Larder. We are in the process of re-branding at the moment and want to use the new brand for the logo. The new website is still under development but you can have a look at it here: http://rosemaryslarder.sitevane.net/minimal-layout The product we want to market i the flyer are our ready-made meals. We are marketing to the corporate world. The meals are intended to be purchased by large firms to feed their staff that are working back late after-hours. They are home-made, fresh, healthy, convenient and most importantly - delicious! You can find the menu and a brief explanation of the ready-made meals on the website. I thought that we might include the menu on the backside of the flyer but i am not set on this.

We want to provide an introductory offer of 10 meals for $100 (usually $130).

I have attached an image of where i got to with the flyer just for your information. You can see why i need your assistance!

I should also add that the logo is intended to be printed in a gold foil! Added Wednesday, February 3, 2016

Target Market(s)

Corporate market - this doesnt mean boring though. It wont be the big bosses who read this flyer it will be the catering managers - they are likely to see a lot of flyers so this one needs to stand out.

Industry/Entity Type

Catering

Requirements
Must have
• Must have the logo! Keep in mind the logo will be printed in a gold foil so it will be very metallic.
• Must reference introductory offer of 10 meals for $100.
• Must have website.
Nice to have
• Would like to see the menu on the backside - i am flexible with this if you have a better idea.
Should not have
• no cartoony images

```html
<!DOCTYPE html>
<html lang="en">
<head>
<meta charset="utf-8">
<title>Rosemary's Larder – Introductory Offer Flyer</title>
<link href="https://fonts.googleapis.com/css2?family=Arimo:wght@400;700&family=Raleway:wght@200;500&display=swap" rel="stylesheet">
<style>
  :root {
    --stage: #8f8d8c;
    --stage-dark: #5e5c5b;
    --marble-light: #f4f4f4;
    --marble-mid: #e2e2e3;
    --band-grey: #cfcfd0;
    --panel-white: rgba(255, 255, 255, 0.92);
    --gold-light: #d9bf5a;
    --gold: #c4a337;
    --gold-dark: #a8872a;
    --ink: #1b1b1b;
    --ink-soft: #333333;
    --white: #ffffff;
  }
  * { box-sizing: border-box; margin: 0; padding: 0; }
  html, body {
    width: 1200px;
    height: 1044px;
    overflow: hidden;
  }
  body {
    background: radial-gradient(ellipse at 50% 55%, var(--stage) 0%, var(--stage-dark) 100%);
    display: flex;
    align-items: center;
    justify-content: center;
    font-family: "Arimo", Arial, sans-serif;
  }
  .flyer {
    position: relative;
    width: 600px;
    height: 848px;
    background: linear-gradient(160deg, var(--marble-light) 0%, var(--marble-mid) 45%, var(--marble-light) 70%, var(--marble-mid) 100%);
    box-shadow: 0 20px 40px rgba(0, 0, 0, 0.35);
    overflow: hidden;
  }
  .flyer__band {
    position: absolute;
    left: 0;
    top: 205px;
    width: 100%;
    height: 130px;
    background: var(--band-grey);
    opacity: 0.85;
  }
  .brand-mark {
    position: absolute;
    left: 50%;
    top: 40px;
    width: 190px;
    height: 190px;
    margin-left: -95px;
    border-radius: 50%;
    background: radial-gradient(circle at 35% 30%, var(--gold-light) 0%, var(--gold) 55%, var(--gold-dark) 100%);
    display: flex;
    align-items: center;
    justify-content: center;
    text-align: center;
    z-index: 2;
  }
  .brand-mark__name {
    font-family: "Raleway", Arial, sans-serif;
    font-weight: 500;
    font-size: 26px;
    line-height: 1.15;
    color: var(--white);
  }
  .offer {
    position: absolute;
    left: 0;
    top: 238px;
    width: 100%;
    text-align: center;
    z-index: 1;
  }
  .offer__kicker {
    font-family: "Raleway", Arial, sans-serif;
    font-weight: 200;
    font-size: 34px;
    letter-spacing: 1px;
    color: var(--ink);
  }
  .offer__deal {
    font-family: "Arimo", Arial, sans-serif;
    font-weight: 700;
    font-size: 44px;
    color: var(--ink);
    margin-top: 2px;
  }
  .intro {
    position: absolute;
    left: 0;
    top: 335px;
    width: 100%;
    height: 190px;
    background: var(--panel-white);
    padding: 22px 40px 0;
    text-align: center;
    color: var(--ink-soft);
    font-size: 15px;
    line-height: 1.4;
  }
  .intro p + p { margin-top: 14px; }
  .intro__link {
    display: inline-block;
    margin-top: 14px;
    padding: 5px 22px;
    border-radius: 14px;
    background: var(--gold);
    color: var(--ink);
    font-size: 13px;
  }
  .intro__link strong { font-weight: 700; }
  .gallery {
    position: absolute;
    left: 0;
    top: 525px;
    width: 100%;
    height: 323px;
    display: grid;
    grid-template-columns: 1.2fr 1fr 1fr;
    grid-template-rows: 1fr 1fr;
    gap: 6px;
    background: var(--white);
    padding-top: 6px;
  }
  .gallery__photo { width: 100%; height: 100%; }
  .gallery__photo--rolls { grid-row: span 2; background: linear-gradient(150deg, #d9a35e, #b8763a 55%, #7d8a3c); }
  .gallery__photo--gift { background: linear-gradient(140deg, #8a6a45, #c9a67a 60%, #a8c3bd); }
  .gallery__photo--boxes { background: linear-gradient(140deg, #e8dcc8, #cdb896 60%, #f1ebe0); }
  .gallery__photo--bagels { background: linear-gradient(140deg, #b06a34, #d89a58 55%, #c43a3a); }
  .gallery__photo--lunch { background: linear-gradient(140deg, #e7d9c0, #c3803f 50%, #e8b74a); }
</style>
</head>
<body>
  <main class="flyer">
    <div class="flyer__band"></div>

    <div class="brand-mark">
      <span class="brand-mark__name">Rosemary's<br>Larder</span>
    </div>

    <header class="offer">
      <h1 class="offer__kicker">INTRODUCTORY OFFER!</h1>
      <p class="offer__deal">10 meals for $100</p>
    </header>

    <section class="intro">
      <p>Looking for a way to keep your staff working hard after hours?<br>We have the solution.</p>
      <p>Our home-made meals are a great, convenient solution! With<br>our meals on hand, your staff will never go hungry on those<br>late nights at the office.</p>
      <span class="intro__link">Visit : <strong>www.rosemaryslarder.com.au</strong></span>
    </section>

    <section class="gallery">
      <div class="gallery__photo gallery__photo--rolls" role="img" aria-label="Photo of filled bread rolls with ham, rocket and mustard dressing"></div>
      <div class="gallery__photo gallery__photo--gift" role="img" aria-label="Photo of a wrapped bag of biscuits with a branded tag"></div>
      <div class="gallery__photo gallery__photo--boxes" role="img" aria-label="Photo of rows of packed cookie boxes"></div>
      <div class="gallery__photo gallery__photo--bagels" role="img" aria-label="Photo of bagels, pastries and strawberries in takeaway trays"></div>
      <div class="gallery__photo gallery__photo--lunch" role="img" aria-label="Photo of a boxed lunch with a baguette, salad cup and custard tart"></div>
    </section>
  </main>
</body>
</html>
```